Create a memorable Stationary for Security Software Company

TalbrenQuay is the worldwide leader in securing the Internet. Making Internet communications and critical data secure, reliable and available everywhere has been and continues to be our ongoing vision. We are committed to staying focused on real customer needs and to developing new and innovative security solutions that redefine the security landscape.

Industry/Entity Type

Internet

Font styles to use
Serif
Sans Serif
Script

Colors
0792cd
33a6d7
85cae6

```html
<!DOCTYPE html>
<html lang="en">
<head>
<meta charset="utf-8">
<title>TalbrenQuay Business Card</title>
<link rel="stylesheet" href="https://fonts.googleapis.com/css2?family=Open+Sans:wght@400;600;700&display=swap">
<style>
  :root {
    --blue-deep: #0792cd;
    --blue-mid: #33a6d7;
    --blue-light: #85cae6;
    --white: #ffffff;
    --backdrop: #eef1f4;
  }
  * { box-sizing: border-box; margin: 0; padding: 0; }
  html, body {
    width: 1200px;
    height: 1120px;
    overflow: hidden;
    background: var(--backdrop);
    font-family: "Open Sans", Arial, sans-serif;
  }
  .stage {
    position: relative;
    width: 1200px;
    height: 1120px;
  }
  .card {
    position: absolute;
    width: 720px;
    height: 410px;
    overflow: hidden;
    box-shadow: 0 10px 30px rgba(0, 0, 0, 0.18);
  }

  /* Front */
  .card-front {
    left: 110px;
    top: 90px;
    background: var(--blue-deep);
  }
  .front-brand {
    position: absolute;
    left: 0;
    right: 0;
    top: 120px;
    display: flex;
    align-items: center;
    justify-content: center;
    gap: 16px;
  }
  .brand-dot {
    width: 46px;
    height: 46px;
    border-radius: 50%;
    background: var(--blue-mid);
  }
  .front-brand .brand-name {
    font-size: 46px;
    font-weight: 700;
    color: var(--blue-light);
  }
  .front-web {
    position: absolute;
    left: 0;
    right: 0;
    top: 318px;
    text-align: center;
    font-size: 22px;
    letter-spacing: 4px;
    color: var(--white);
  }

  /* Back */
  .card-back {
    left: 380px;
    top: 620px;
    background: var(--blue-light);
  }
  .back-shapes {
    position: absolute;
    inset: 0;
  }
  .back-brand {
    position: absolute;
    left: 40px;
    top: 182px;
    display: flex;
    align-items: center;
    gap: 12px;
  }
  .back-brand .brand-dot {
    width: 38px;
    height: 38px;
    background: var(--blue-deep);
  }
  .back-brand .brand-name {
    font-size: 36px;
    font-weight: 700;
    color: var(--blue-mid);
  }
  .contact-block {
    position: absolute;
    right: 40px;
    top: 40px;
    text-align: right;
    color: var(--white);
  }
  .person-name {
    font-size: 22px;
    font-weight: 700;
    line-height: 1.2;
  }
  .person-title {
    font-size: 18px;
    line-height: 1.3;
    margin-bottom: 28px;
  }
  .contact-list {
    list-style: none;
    font-size: 17px;
    line-height: 1.25;
  }
  .contact-list li {
    display: flex;
    justify-content: flex-end;
    align-items: flex-start;
    gap: 8px;
    margin-bottom: 8px;
  }
  .contact-list svg {
    width: 15px;
    height: 15px;
    flex: none;
    margin-top: 3px;
    fill: var(--white);
  }
  .contact-list .address { margin-top: 8px; }
</style>
</head>
<body>
<main class="stage">

  <section class="card card-front">
    <div class="front-brand">
      <span class="brand-dot"></span>
      <span class="brand-name">TalbrenQuay</span>
    </div>
    <p class="front-web">www.talbrenquay.com</p>
  </section>

  <section class="card card-back">
    <svg class="back-shapes" viewBox="0 0 720 410" width="720" height="410" aria-hidden="true">
      <circle cx="640" cy="200" r="312" fill="var(--blue-mid)"/>
      <circle cx="650" cy="200" r="304" fill="var(--blue-light)"/>
      <circle cx="658" cy="200" r="300" fill="var(--blue-deep)"/>
    </svg>

    <div class="back-brand">
      <span class="brand-dot"></span>
      <span class="brand-name">TalbrenQuay</span>
    </div>

    <div class="contact-block">
      <p class="person-name">Your Name</p>
      <p class="person-title">Title</p>
      <ul class="contact-list">
        <li>
          <svg viewBox="0 0 16 16"><path d="M4 1l3 3-2 2c1 2 3 4 5 5l2-2 3 3-2 3C7 15 1 9 1 3z"/></svg>
          <span>012-345-6789</span>
        </li>
        <li>
          <svg viewBox="0 0 16 16"><path d="M4 0h8v16H4z M5.5 2v9h5V2z M7 12.5h2v2H7z" fill-rule="evenodd"/></svg>
          <span>012-345-6789</span>
        </li>
        <li>
          <svg viewBox="0 0 16 16"><path d="M1 3h14v10H1z M2 4l6 5 6-5z" fill-rule="evenodd"/></svg>
          <span>info@talbrenquay.com</span>
        </li>
        <li>
          <svg viewBox="0 0 16 16"><path d="M8 0a8 8 0 100 16A8 8 0 008 0zm0 1.5c1 1 1.7 3 1.9 5.5H6.1C6.3 4.5 7 2.5 8 1.5zM1.6 7h3c.1-2 .6-3.7 1.3-5A6.5 6.5 0 001.6 7zm0 2a6.5 6.5 0 004.3 5c-.7-1.3-1.2-3-1.3-5zm4.5 0h3.8c-.2 2.5-.9 4.5-1.9 5.5-1-1-1.7-3-1.9-5.5zm5.3 0c-.1 2-.6 3.7-1.3 5a6.5 6.5 0 004.3-5zm3-2a6.5 6.5 0 00-4.3-5c.7 1.3 1.2 3 1.3 5z"/></svg>
          <span>www.talbrenquay.com</span>
        </li>
        <li class="address">
          <svg viewBox="0 0 16 16"><path d="M8 0a6 6 0 016 6c0 4-6 10-6 10S2 10 2 6a6 6 0 016-6zm0 3.5a2.5 2.5 0 100 5 2.5 2.5 0 000-5z" fill-rule="evenodd"/></svg>
          <span>Street Name, City Name<br>Zipcode-012345</span>
        </li>
      </ul>
    </div>
  </section>

</main>
</body>
</html>
```